Exciting Wordpress Project: New Consulting Firm

A wordpress design is needed for my new consulting company, Brellow Advisory.

The site should have a modern feel to it and use the colour scheme from the attached 3 vector files.

I only know a little about Wordpress but the site should be mobile friendly.

The following menu options should be created:
1. Home
2. Brellow service lines (with sub-menus)
3. Our people
4. Brellow case studies
5. The Brellow story
6. Contact Brellow
Updates

Project Deadline Extended
Reason: Allow just one or two more designs to come in before deciding.

Target Market(s)

Government departments and medium private sector organisations

Industry/Entity Type

It Company

Requirements
Must have
• 1. Inclue Brellow logo at top of each page
2. Slider on the home page
3. Global navigation
4. Drop down navigation
5. Social media links
6. Search and contact details at the top of the home page
7. Home page to fit on one screen
8. Terms & Conditions, Privacy Policy at the bottom of the home page
9. Newsletter (i.e. postwren) subscription on home page
Nice to have
• 1. Background watermark from the Brellow logo
2. A layout similar to the photo attached - however open to different ideas

```html
<!DOCTYPE html>
<html lang="en">
<head>
<meta charset="utf-8">
<title>Brellow Advisory</title>
<link href="https://fonts.googleapis.com/css2?family=Arimo:wght@400;700&display=swap" rel="stylesheet">
<style>
  :root {
    --brand-blue: #2b5fb1;
    --brand-blue-dark: #1f4f9e;
    --heading-blue: #2957a8;
    --text-grey: #6b6b6b;
    --text-dark: #3a3a3a;
    --logo-grey: #5f6063;
    --rule: #dcdcdc;
    --card-top: #d6e0ef;
    --card-bottom: #ffffff;
    --footer-top: #e4e4e4;
    --footer-bottom: #ffffff;
    --watermark: rgba(120, 120, 120, 0.07);
    --page-bg: #ffffff;
  }
  * { box-sizing: border-box; margin: 0; padding: 0; }
  html, body {
    width: 1126px; height: 1200px; overflow: hidden;
    background: var(--page-bg);
    font-family: "Arimo", Arial, sans-serif;
    color: var(--text-grey);
  }
  .page { position: relative; width: 1126px; height: 1200px; }

  .brand {
    position: absolute; left: 62px; top: 26px;
    color: var(--logo-grey); font-weight: 400;
    font-size: 38px; letter-spacing: 1px; line-height: 1;
  }
  .brand-sub {
    position: absolute; left: 62px; top: 62px;
    color: var(--logo-grey); font-size: 10px; letter-spacing: 13.5px;
  }

  .main-nav {
    position: absolute; left: 50px; top: 92px; width: 1000px; height: 45px;
    background: var(--brand-blue); display: flex;
  }
  .main-nav a {
    color: #fff; text-decoration: none; font-weight: 700; font-size: 12.5px;
    display: flex; align-items: center; justify-content: center;
    border-right: 1px solid rgba(255,255,255,0.18); height: 100%;
  }
  .main-nav a:last-child { border-right: none; }

  .slide { position: absolute; top: 151px; height: 342px; border-radius: 4px; }
  .slide-side {
    left: 50px; width: 273px;
    background: linear-gradient(160deg, #6aa0e0 0%, #1e58b0 45%, #0d3478 100%);
  }
  .slide-main {
    left: 333px; width: 717px;
    background: linear-gradient(135deg, #1d3a6e 0%, #c9b79c 35%, #d9cdb8 55%, #2a3f6a 80%, #1a2740 100%);
  }
  .slider-dots { position: absolute; right: 22px; bottom: 16px; display: flex; gap: 4px; }
  .slider-dots span { width: 9px; height: 9px; background: #c9c9c9; }
  .slider-dots span:first-child { background: #e6e6e6; }

  .feature {
    position: absolute; top: 518px; width: 315px; height: 123px;
    background: linear-gradient(to bottom, var(--card-top), var(--card-bottom));
    border: 1px solid #e8edf5;
  }
  .feature-title {
    position: absolute; left: -1px; top: 13px; width: 227px; height: 33px;
    background: var(--brand-blue); color: #fff; font-size: 15px;
    padding: 9px 0 0 29px;
  }
  .feature-text {
    position: absolute; left: 31px; top: 50px; width: 270px;
    font-size: 12px; line-height: 16px; color: var(--text-grey);
  }

  .watermark {
    position: absolute; left: 0; width: 1126px; text-align: center;
    color: var(--watermark); font-weight: 700; pointer-events: none;
  }
  .watermark-main { top: 615px; font-size: 190px; letter-spacing: 40px; left: 30px; }
  .watermark-sub { top: 808px; font-size: 48px; letter-spacing: 76px; left: 40px; }

  .section-title {
    position: absolute; color: var(--heading-blue);
    font-weight: 700; font-size: 15px; letter-spacing: 0.3px;
  }
  .body-text { position: absolute; font-size: 12px; line-height: 17px; color: var(--text-grey); }

  .team-photo {
    position: absolute; left: 56px; top: 699px; width: 138px; height: 75px;
    background: linear-gradient(120deg, #c8c2bb 0%, #8b8f9a 50%, #dcdcdc 100%);
  }

  .subscribe-field {
    position: absolute; left: 740px; top: 722px; width: 262px; height: 37px;
    border: 1px solid #e2e2e2; background: #fff;
  }
  .subscribe-field svg { position: absolute; right: 4px; top: 5px; }

  .divider { position: absolute; left: 50px; top: 794px; width: 1000px; height: 1px; background: var(--rule); }

  .link-title {
    position: absolute; color: var(--heading-blue); font-weight: 700;
    font-size: 12.5px; line-height: 17px;
  }
  .more-link { position: absolute; left: 738px; top: 995px; font-size: 12.5px; color: var(--heading-blue); }

  .site-footer {
    position: absolute; left: 50px; top: 1030px; width: 1000px; height: 130px;
    background: linear-gradient(to bottom, var(--footer-top), var(--footer-bottom));
    border-top: 1px solid #d2d2d2;
  }
  .footer-nav { position: absolute; left: 15px; top: 22px; display: flex; gap: 16px; }
  .footer-nav a { color: var(--text-dark); text-decoration: none; font-weight: 700; font-size: 12.5px; }
  .copyright { position: absolute; left: 15px; top: 52px; color: var(--text-dark); font-weight: 700; font-size: 12.5px; }
  .social { position: absolute; right: 21px; top: 15px; display: flex; gap: 3px; }
  .social span { width: 28px; height: 28px; border-radius: 3px; }
  .social .social-one { background: #39a6e0; }
  .social .social-two { background: #3b5a98; }
</style>
</head>
<body>
<div class="page">

  <div class="brand">BRELLOW</div>
  <div class="brand-sub">ADVISORY</div>

  <nav class="main-nav">
    <a href="#" style="width:82px">Home</a>
    <a href="#" style="width:178px">Brellow service lines</a>
    <a href="#" style="width:131px">Our people</a>
    <a href="#" style="width:181px">Brellow case studies</a>
    <a href="#" style="width:181px">The Brellow story</a>
    <a href="#" style="width:247px">Contact Brellow</a>
  </nav>

  <div class="slide slide-side" role="img" aria-label="Glass office tower against a blue sky"></div>
  <div class="slide slide-main" role="img" aria-label="Business team working at a table with laptop and documents">
    <div class="slider-dots"><span></span><span></span><span></span><span></span><span></span></div>
  </div>

  <div class="watermark watermark-main">BRELLOW</div>
  <div class="watermark watermark-sub">ADVISORY</div>

  <div class="feature" style="left:50px">
    <div class="feature-title" style="top:14px">Tempor inciunt ut labore</div>
    <p class="feature-text">Lorem ipsum dolor sit amet, consectetur adipisic elit, sed do eiusmod tempor incidunt ut labore et dolore magna aliqua. Ut enim ad minim veniam</p>
  </div>
  <div class="feature" style="left:393px">
    <div class="feature-title">Tempor inciunt ut labore</div>
    <p class="feature-text" style="left:28px">Lorem ipsum dolor sit amet, consectetur adipisic elit, sed do eiusmod tempor incidunt ut labore et dolore magna aliqua. Ut enim ad minim veniam</p>
  </div>
  <div class="feature" style="left:744px">
    <div class="feature-title">Tempor inciunt ut labore</div>
    <p class="feature-text" style="left:18px">Lorem ipsum dolor sit amet, consectetur adipisic elit, sed do eiusmod tempor incidunt ut labore et dolore magna aliqua. Ut enim ad minim veniam</p>
  </div>

  <h2 class="section-title" style="left:57px;top:675px">CONSULTING PROGRAM</h2>
  <div class="team-photo" role="img" aria-label="Group of colleagues gathered around a laptop"></div>
  <p class="body-text" style="left:207px;top:704px;width:480px">Sed ut perspiciatis unde omnis iste natus error sit voluptatem accusantium doloremque laudantium, totam rem aperiam ab illo inventore veritatis et quasi architecto beatae vitae dicta sunt explicabo. Nemo enim ipsam voluptatem quia volup aut odit aut fugit, sed quia consequuntur magni dolores eos qui ratione voluptatem sequi nesciunt.</p>

  <h2 class="section-title" style="left:738px;top:675px">SUBSCRIBE</h2>
  <p class="body-text" style="left:738px;top:703px">Sed ut perspiciatis unde omnis iste natus error sit</p>
  <div class="subscribe-field">
    <svg width="36" height="28" viewBox="0 0 36 28" aria-hidden="true">
      <rect x="2" y="2" width="26" height="19" fill="#fff" stroke="#9a9a9a" stroke-width="1.2"/>
      <polyline points="2,2 15,13 28,2" fill="none" stroke="#9a9a9a" stroke-width="1.2"/>
      <path d="M20 19 h7 v-4 l7 6 l-7 6 v-4 h-7 z" fill="#5cb531"/>
    </svg>
  </div>

  <div class="divider"></div>

  <h2 class="section-title" style="left:57px;top:836px">CASE STUDIES</h2>
  <p class="link-title" style="left:60px;top:861px;width:520px">Sed ut perspiciatis unde omnis iste natus error sit voluptatem accusantium doloremque laudantium</p>
  <p class="body-text" style="left:61px;top:904px;width:600px">Sed ut perspiciatis unde omnis iste natus error sit voluptatem accusantium doloremque laudantium, totam rem aperiam ab illo inventore veritatis et quasi architecto beatae vitae dicta sunt explicabo. Nemo enim ipsam voluptatem quia volup aut odit aut fugit, sed quia consequuntur magni dolores eos qui ratione voluptatem sequi nesciunt.</p>

  <h2 class="section-title" style="left:738px;top:836px">EVENTS</h2>
  <p class="link-title" style="left:737px;top:865px">Sed ut perspiciatis unde omnis 15, May, 2013</p>
  <p class="body-text" style="left:737px;top:890px;width:265px">Lorem ipsum dolor sit amet, consectetur adipisic elit, sed do eiusmod tempor</p>
  <p class="link-title" style="left:737px;top:936px">Sed ut perspiciatis unde omnis 15, May, 2013</p>
  <p class="body-text" style="left:737px;top:956px;width:265px">Lorem ipsum dolor sit amet, consectetur adipisic elit, sed do eiusmod tempor</p>
  <a class="more-link" href="#">View more..</a>

  <footer class="site-footer">
    <nav class="footer-nav">
      <a href="#">Home</a>
      <a href="#">Brellow service lines</a>
      <a href="#">Our people</a>
      <a href="#">Brellow case studies</a>
      <a href="#">The Brellow story</a>
      <a href="#">Contact Brellow</a>
    </nav>
    <p class="copyright">Copyrights 2013. All rights reserved.</p>
    <div class="social"><span class="social-one"></span><span class="social-two"></span></div>
  </footer>

</div>
</body>
</html>
```